Velm Otter

I want a design for a website where users can insert products URLs from different sites and the user will get notified by email when that product's price changes.

On the homepage I'd like a big input where the user can insert a product's URL. On the same page the following will appear:
- my products that I follow (options: share, buy, unfollow) + it's current price and deviation from last time it's price has changed (I may have many products that I follow, so maybe a table layout would be wise. - just a suggestion)
- products that other people follow (options: follow). If my Quillmark friends follow a certain product, I can see their photo(eg: friend1, friend2 and 5 others are following this product) (also, may people may follow a product.)

On the login page I can register using user / pass or using Quillmark

The 3rd page is the product's page. Once I click on any product I go to this page. On this page I can see:
- picture, name and price and no of people following this product
- a chart with the product's price over the last 30 days
- list with friends that follow this product (when logged in)
- product options: follow / unfollow, share, buy

Then I want the design for an email template that I send when 1 or more prices of a user's products change.

Nice to have: want level for product - describes how much wanted is a product after a certain internal algorithm

NB:
- flat design (not really pivra, something more like the new Zyx interface - just a suggestion)
- I'd prefer a red theme (based on the idea that the site will be represented by a rooster)
- don't forget the design for basic elements: loading screen, popup, alert, messages, etc

I've posted an initial prototype with what I'd like the design to contain.

• - flat design
- must be simple. much white space
• as few gradients as possible

```html
<!DOCTYPE html>
<html lang="en">
<head>
<meta charset="utf-8">
<title>Velm Otter – Track product prices</title>
<link href="https://fonts.googleapis.com/css2?family=Arimo:wght@400;700&display=swap" rel="stylesheet">
<style>
:root{
  --ink:#1c1c1c;
  --red:#db5a4b;
  --red-deep:#c7463a;
  --price:#cc0000;
  --blue:#3d8ee8;
  --row:#e6e6e6;
  --card:#f2f2f2;
  --white:#ffffff;
  --text:#111111;
  --btn-border:#c9c9c9;
  --muted:#9a9a9a;
}
*{box-sizing:border-box;margin:0;padding:0}
html,body{width:983px;height:1200px;overflow:hidden;background:var(--white);font-family:"Arimo",Arial,sans-serif;color:var(--text)}
.page{position:relative;width:983px;height:1200px}

/* header */
.site-header{position:absolute;left:0;top:0;width:983px;height:102px;background:var(--ink)}
.brand{position:absolute;left:48px;top:33px;display:flex;align-items:center;gap:9px;color:var(--white);font-weight:700;font-size:32px;letter-spacing:-0.5px}
.brand-mark{width:14px;height:14px;background:var(--red)}
.main-nav{position:absolute;top:42px;left:0;font-size:15.5px;color:var(--white)}
.main-nav a{position:absolute;white-space:nowrap;color:inherit;text-decoration:none}
.account{position:absolute;top:40px;height:23px;border-radius:3px;background:#3a3a3a;color:var(--muted);font-size:12px;line-height:23px;padding-left:27px}
.account svg{position:absolute;left:7px;top:6px}
.account.login{left:821px;width:62px}
.account.register{left:890px;width:72px}

/* hero */
.hero{position:absolute;left:0;top:102px;width:983px;height:246px;background:var(--red)}
.track-form{position:absolute;left:247px;top:94px;width:489px;height:57px;border-radius:9px;background:var(--red-deep)}
.track-input{position:absolute;left:6px;top:6px;width:374px;height:46px;background:var(--white);border:0;border-radius:6px 0 0 6px}
.track-button{position:absolute;left:379px;top:6px;width:106px;height:46px;border-radius:0 6px 6px 0;background:linear-gradient(#3a3a3a,#111);color:var(--white);font-size:18px;line-height:46px;text-align:center}

/* followed products */
.followed{position:absolute;left:16px;top:367px;width:950px}
.product-row{position:absolute;left:0;width:950px;height:100px;background:var(--row);border-top:4px solid var(--red)}
.product-thumb{position:absolute;left:10px;top:8px;width:72px;height:72px;background:linear-gradient(135deg,#ffffff,#d9d9d9);border-left:2px solid var(--red);border-bottom:2px solid var(--red)}
.product-name{position:absolute;left:101px;top:14px;font-size:27px;font-weight:400;color:var(--blue)}
.product-desc{position:absolute;left:101px;top:54px;font-size:11.5px;line-height:15.5px}
.price{position:absolute;left:391px;top:58px;font-size:17px;color:var(--price)}
.delta{position:absolute;left:572px;top:58px;font-size:17px;color:var(--price)}
.action{position:absolute;top:52px;width:75px;height:31px;border:1px solid var(--btn-border);border-radius:3px;background:linear-gradient(#ffffff,#f3f3f3);font-size:11.5px;line-height:29px;text-align:center;color:#333}
.action.share{left:696px}
.action.buy{left:781px}
.action.unfollow{left:865px}

/* others follow */
.section-title{position:absolute;left:16px;top:795px;width:383px;height:43px;background:var(--red);clip-path:polygon(0 0,364px 0,383px 43px,0 43px);color:var(--white);font-size:21px;font-weight:400;line-height:43px;padding-left:15px;white-space:nowrap}
.section-rule{position:absolute;left:16px;top:839px;width:950px;height:4px;background:#e8e8e8}
.others{position:absolute;left:0;top:901px}
.card{position:absolute;top:0;width:133px;height:150px;background:var(--card);border-right:1px solid #dcdcdc;border-bottom:1px solid #dcdcdc}
.card-flag{position:absolute;left:0;top:0;width:133px;height:44px;background:var(--blue);clip-path:polygon(0 0,133px 0,133px 24px,0 44px)}
.card-name{position:absolute;left:9px;top:5px;font-size:16px;color:var(--white)}
.card-photo{position:absolute;left:16px;top:54px;width:102px;height:76px;background:radial-gradient(ellipse at center,#bdbdbd 0%,#e6e6e6 60%,var(--card) 100%)}
.friends{position:absolute;top:158px;left:0;width:133px;height:27px}
.friend{position:absolute;top:0;width:27px;height:27px;background:linear-gradient(135deg,#8a3a2c,#c8a08e)}
.friend:nth-child(1){left:1px}.friend:nth-child(2){left:33px}.friend:nth-child(3){left:65px}
.more{position:absolute;left:112px;top:4px;font-size:17px;color:var(--price)}

/* footer */
.site-footer{position:absolute;left:0;top:1158px;width:983px;height:42px;background:var(--ink);color:var(--white);font-size:13px;line-height:42px}
.site-footer span{position:absolute;top:0}
</style>
</head>
<body>
<div class="page">

  <header class="site-header">
    <div class="brand"><span>Velm Otter</span><span class="brand-mark"></span></div>
    <nav class="main-nav">
      <a style="left:413px">HOME</a>
      <a style="left:501px">BROWSE PRODUCTS</a>
      <a style="left:699px">CONTACT</a>
    </nav>
    <div class="account login">
      <svg width="13" height="11" viewBox="0 0 13 11"><rect x="6" y="0" width="7" height="11" fill="#8a8a8a"/><path d="M0 5.5h6M4 3l2.5 2.5L4 8" stroke="#8a8a8a" stroke-width="2" fill="none"/></svg>
      Login
    </div>
    <div class="account register">
      <svg width="12" height="11" viewBox="0 0 12 11"><rect x="0" y="0" width="12" height="3" fill="#8a8a8a"/><rect x="2" y="4" width="8" height="3" fill="#8a8a8a"/><rect x="4" y="8" width="4" height="3" fill="#8a8a8a"/></svg>
      Register
    </div>
  </header>

  <section class="hero">
    <form class="track-form">
      <input class="track-input" type="text" aria-label="Product URL">
      <div class="track-button">Follow</div>
    </form>
  </section>

  <section class="followed">
    <article class="product-row" style="top:0">
      <div class="product-thumb" role="img" aria-label="Product photo: white kitchen knife block"></div>
      <h2 class="product-name">Torvelle</h2>
      <p class="product-desc">Lorem Ipsum is simply dummy text<br>of the printing and typesetting industry.</p>
      <span class="price">450 USD</span><span class="delta">+4 USD</span>
      <div class="action share">Share</div><div class="action buy">Buy</div><div class="action unfollow">Unfollow</div>
    </article>
    <article class="product-row" style="top:120px">
      <div class="product-thumb" role="img" aria-label="Product photo: yellow safety helmet" style="background:linear-gradient(135deg,#ffffff 30%,#f0c040 60%,#ffffff)"></div>
      <h2 class="product-name">Casklin</h2>
      <p class="product-desc">Lorem Ipsum is simply dummy text<br>of the printing and typesetting industry.</p>
      <span class="price">450 USD</span><span class="delta">+4 USD</span>
      <div class="action share">Share</div><div class="action buy">Buy</div><div class="action unfollow">Unfollow</div>
    </article>
    <article class="product-row" style="top:241px">
      <div class="product-thumb" role="img" aria-label="Product photo: electric bicycle"></div>
      <h2 class="product-name">Ulmeno</h2>
      <p class="product-desc">Lorem Ipsum is simply dummy text<br>of the printing and typesetting industry.</p>
      <span class="price">450 USD</span><span class="delta">+4 USD</span>
      <div class="action share">Share</div><div class="action buy">Buy</div><div class="action unfollow">Unfollow</div>
    </article>
  </section>

  <h2 class="section-title">Products that other people follow</h2>
  <div class="section-rule"></div>

  <section class="others">
    <article class="card" style="left:17px">
      <div class="card-flag"></div>
      <span class="card-name">Ulmeno</span>
      <div class="card-photo" role="img" aria-label="Product photo: electric bicycle"></div>
      <div class="friends"><i class="friend" role="img" aria-label="Friend avatar"></i><i class="friend" role="img" aria-label="Friend avatar"></i><i class="friend" role="img" aria-label="Friend avatar"></i><span class="more">+5</span></div>
    </article>
    <article class="card" style="left:179px">
      <div class="card-flag"></div>
      <span class="card-name">Ulmeno</span>
      <div class="card-photo" role="img" aria-label="Product photo: electric bicycle"></div>
      <div class="friends"><i class="friend" role="img" aria-label="Friend avatar"></i><i class="friend" role="img" aria-label="Friend avatar"></i><i class="friend" role="img" aria-label="Friend avatar"></i><span class="more">+5</span></div>
    </article>
    <article class="card" style="left:344px">
      <div class="card-flag"></div>
      <span class="card-name">Ulmeno</span>
      <div class="card-photo" role="img" aria-label="Product photo: electric bicycle"></div>
      <div class="friends"><i class="friend" role="img" aria-label="Friend avatar"></i><i class="friend" role="img" aria-label="Friend avatar"></i><i class="friend" role="img" aria-label="Friend avatar"></i><span class="more">+5</span></div>
    </article>
    <article class="card" style="left:505px">
      <div class="card-flag"></div>
      <span class="card-name">Ulmeno</span>
      <div class="card-photo" role="img" aria-label="Product photo: electric bicycle"></div>
      <div class="friends"><i class="friend" role="img" aria-label="Friend avatar"></i><i class="friend" role="img" aria-label="Friend avatar"></i><i class="friend" role="img" aria-label="Friend avatar"></i><span class="more">+5</span></div>
    </article>
    <article class="card" style="left:670px">
      <div class="card-flag"></div>
      <span class="card-name">Ulmeno</span>
      <div class="card-photo" role="img" aria-label="Product photo: electric bicycle"></div>
      <div class="friends"><i class="friend" role="img" aria-label="Friend avatar"></i><i class="friend" role="img" aria-label="Friend avatar"></i><i class="friend" role="img" aria-label="Friend avatar"></i><span class="more">+5</span></div>
    </article>
    <article class="card" style="left:832px">
      <div class="card-flag"></div>
      <span class="card-name">Ulmeno</span>
      <div class="card-photo" role="img" aria-label="Product photo: electric bicycle"></div>
      <div class="friends"><i class="friend" role="img" aria-label="Friend avatar"></i><i class="friend" role="img" aria-label="Friend avatar"></i><i class="friend" role="img" aria-label="Friend avatar"></i><span class="more">+5</span></div>
    </article>
  </section>

  <footer class="site-footer">
    <span style="left:21px">Disclaimer</span>
    <span style="left:125px">Company 2013</span>
  </footer>

</div>
</body>
</html>
```